Price list for young Relaxa clinic

I require a price list/Treatment menu for clinic

To include:
Logo
Address
Phone number
Website

List of services and Prices
Relaxa 1 area £100
Relaxa 2 areas £150
Relaxa 3 areas £200
Lip Enhancement 0.5ml £100
Lip Enhancement 1ml £200
Facial Fillers £200 per 1ml
Vivorel £450 per session (2 vials - must be bought as a course)
Non Surgical Face Lift (Thread Lift) £600 per area
Micro Stamp Full Face £250
Micro Stamp Small Per Small Area £100
Cryo Therapy £60
Chemical Peel Light Peel and Microdermabrasion £85
Chemical Peel Deep Peel £150
Consultation £30 redeemable against service
Relaxa Top Up Relaxa £50 (must be within 2 weeks of 1st treatment)
Filler Top Up £100 (must be within 2 weeks of 1st appointment)

Open Hours
Updates

Company Name: MBH Address: 52 Fenwick Lane, 4 Marlow Parade, KT9 3QD Phone: 0208 947 2186 Website: www.mirabellhoughaesthetics.co.uk

Please add more colour

Needs to be much cleaner and simpler Front page to include logo and price list Back page to inculde open hours and contact information including google map. Please no images with needles. Images of lips and faces are good, but try not to crowd copy on the pagei. No copy on top of images. White, grey, black and reds are good on colouring.

Target Market(s)

young market ages 22-45 years old mainly female
modern

Industry/Entity Type

Clinic

Number of Pages Required

4 page

Requirements
Must have
• Logo - logo must be in colour grey/silver
• Address (small map?)
• Phone number
• Web address
• Services
• Open hours
• Prices
• Images

```html
<!DOCTYPE html>
<html lang="en">
<head>
<meta charset="utf-8">
<title>MBH Aesthetics – Treatment Menu</title>
<link href="https://fonts.googleapis.com/css2?family=Questrial&family=Arimo:ital,wght@0,400;0,700;1,400&display=swap" rel="stylesheet">
<style>
:root{
  --backdrop:#d9dbda;
  --paper:#f4f3f4;
  --paper-tint:#ead8e2;
  --ink:#2a2a2a;
  --ink-soft:#555;
  --rule:#9a9a9a;
  --accent:#c2307a;
  --accent-soft:#e78ab8;
  --silver-dark:#6f6f6f;
  --silver-light:#d8d8d8;
  --skin:#c9a28e;
}
*{box-sizing:border-box;margin:0;padding:0}
html,body{width:1200px;height:900px;overflow:hidden}
body{background:var(--backdrop);position:relative;font-family:"Questrial",sans-serif;color:var(--ink)}

.page{position:absolute;top:140px;width:440px;height:620px;overflow:hidden;
  background:linear-gradient(160deg,#ffffff 0%,var(--paper) 40%,var(--paper-tint) 75%,#ffffff 100%);
  box-shadow:0 6px 18px rgba(0,0,0,.25)}
.page--front{left:140px}
.page--back{left:620px}

.accent-band{position:absolute;height:5px;
  background:linear-gradient(90deg,transparent 0%,var(--accent-soft) 30%,var(--accent) 70%,var(--accent) 100%)}
.accent-band--front-top{left:190px;right:0;top:52px}
.accent-band--front-bottom{left:0;right:0;top:466px}
.accent-band--back-top{left:0;right:0;top:66px}
.accent-band--back-middle{left:0;right:0;top:360px}

.damask{position:absolute}
.damask--front-top{right:0;top:0;width:170px;height:52px;
  background:linear-gradient(120deg,transparent 0%,var(--silver-light) 40%,var(--silver-dark) 100%)}
.damask--back-top{right:0;top:0;width:160px;height:66px;
  background:linear-gradient(120deg,transparent 0%,var(--silver-light) 40%,var(--silver-dark) 100%)}
.damask--back-bottom{left:0;top:365px;width:230px;height:255px;
  background:radial-gradient(ellipse at 30% 60%,var(--silver-dark) 0%,var(--silver-light) 55%,transparent 85%)}

/* front */
.brand{position:absolute;left:28px;top:20px;display:flex;flex-direction:column;align-items:flex-start;gap:8px}
.brand__mark{width:48px;height:48px;border-radius:50%;background:var(--silver-dark)}
.brand__name{font-size:14px;letter-spacing:2px;color:var(--ink);line-height:17px}
.price-list{position:absolute;left:28px;right:28px;top:122px}
.price-list__title{text-align:right;font-size:10px;color:var(--ink-soft);margin-bottom:10px;padding-right:40px}
.price-row{display:flex;align-items:baseline;height:19px;font-size:11.5px}
.price-row__name{white-space:nowrap}
.price-row__note{font-size:6.5px;color:var(--ink-soft);margin-left:5px;white-space:nowrap}
.price-row__leader{flex:1;border-bottom:1px dotted var(--rule);margin:0 4px;transform:translateY(-3px)}
.price-row__price{white-space:nowrap}
.feature-image{position:absolute;left:0;top:474px;width:100%;height:146px;
  background:linear-gradient(90deg,var(--silver-light) 0%,var(--silver-dark) 35%,var(--skin) 65%,#e9d5cc 100%)}

/* back */
.contact{position:absolute;left:20px;top:16px;font-family:"Arimo",sans-serif;font-style:italic;font-size:10.5px;line-height:14px;color:var(--ink)}
.hours{position:absolute;left:120px;top:92px;font-family:"Arimo",sans-serif;font-weight:700}
.hours__title{font-size:14px;margin-left:16px;margin-bottom:20px}
.hours__row{font-size:11px;height:26px}
.address{position:absolute;right:22px;top:470px;font-family:"Arimo",sans-serif;font-style:italic;font-size:10px}
.map{position:absolute;right:22px;top:488px;width:212px;height:92px;
  background:linear-gradient(135deg,#ece8e0,#dcd6cb);border:1px solid #b9a98a}
</style>
</head>
<body>

<section class="page page--front" aria-label="Front page – treatment menu">
  <div class="damask damask--front-top" role="img" aria-label="Silver damask ornament"></div>
  <div class="accent-band accent-band--front-top"></div>

  <div class="brand">
    <span class="brand__mark"></span>
    <span class="brand__name">MBH · MIRABELL HOUGH<br>AESTHETICS</span>
  </div>

  <div class="price-list">
    <p class="price-list__title">List of services and Prices</p>
    <div class="price-row"><span class="price-row__name">Relaxa 1 area</span><span class="price-row__leader"></span><span class="price-row__price">£100</span></div>
    <div class="price-row"><span class="price-row__name">Relaxa 2 areas</span><span class="price-row__leader"></span><span class="price-row__price">£150</span></div>
    <div class="price-row"><span class="price-row__name">Relaxa 3 areas</span><span class="price-row__leader"></span><span class="price-row__price">£200</span></div>
    <div class="price-row"><span class="price-row__name">Lip Enhancement 0.5ml</span><span class="price-row__leader"></span><span class="price-row__price">£100</span></div>
    <div class="price-row"><span class="price-row__name">Lip Enhancement 1ml</span><span class="price-row__leader"></span><span class="price-row__price">£200</span></div>
    <div class="price-row"><span class="price-row__name">Facial Fillers</span><span class="price-row__note">per 1ml</span><span class="price-row__leader"></span><span class="price-row__price">£200</span></div>
    <div class="price-row"><span class="price-row__name">Vivorel</span><span class="price-row__note">per session (2 vials - must be bought as a course)</span><span class="price-row__leader"></span><span class="price-row__price">£450</span></div>
    <div class="price-row"><span class="price-row__name">Non Surgical Face Lift (Thread Lift)</span><span class="price-row__note">per area</span><span class="price-row__leader"></span><span class="price-row__price">£600</span></div>
    <div class="price-row"><span class="price-row__name">Micro Stamp Full Face</span><span class="price-row__leader"></span><span class="price-row__price">£250</span></div>
    <div class="price-row"><span class="price-row__name">Micro Stamp Small Per Small Area</span><span class="price-row__leader"></span><span class="price-row__price">£100</span></div>
    <div class="price-row"><span class="price-row__name">Cryo Therapy</span><span class="price-row__leader"></span><span class="price-row__price">£60</span></div>
    <div class="price-row"><span class="price-row__name">Chemical Peel Light Peel and Microdermabrasion</span><span class="price-row__leader"></span><span class="price-row__price">£85</span></div>
    <div class="price-row"><span class="price-row__name">Chemical Peel Deep Peel</span><span class="price-row__leader"></span><span class="price-row__price">£150</span></div>
    <div class="price-row"><span class="price-row__name">Consultation</span><span class="price-row__note">redeemable against service</span><span class="price-row__leader"></span><span class="price-row__price">£30</span></div>
    <div class="price-row"><span class="price-row__name">Relaxa Top Up</span><span class="price-row__note">(must be within 2 weeks of 1st treatment)</span><span class="price-row__leader"></span><span class="price-row__price">£50</span></div>
    <div class="price-row"><span class="price-row__name">Filler Top Up</span><span class="price-row__note">(must be within 2 weeks of 1st appointment)</span><span class="price-row__leader"></span><span class="price-row__price">£100</span></div>
  </div>

  <div class="accent-band accent-band--front-bottom"></div>
  <div class="feature-image" role="img" aria-label="Beauty photograph of a woman's face with dark nails over a silver damask pattern"></div>
</section>

<section class="page page--back" aria-label="Back page – opening times and contact">
  <div class="contact">
    Phone: 0208 947 2186<br>
    Email: mbhmarlowbookings@gmail.com<br>
    Web: www.mirabellhoughaesthetics.co.uk
  </div>
  <div class="damask damask--back-top" role="img" aria-label="Silver damask ornament"></div>
  <div class="accent-band accent-band--back-top"></div>

  <div class="hours">
    <h2 class="hours__title">Opening Times:</h2>
    <p class="hours__row">Monday ......... 10am-4pm</p>
    <p class="hours__row">Tuesday ........ 10am-4pm</p>
    <p class="hours__row">Wednesday ...... 12pm-8pm</p>
    <p class="hours__row">Thursday ....... 7:30am-4:30pm</p>
    <p class="hours__row">(at number 1 Kenworth Street only)</p>
    <p class="hours__row">Friday ......... 10am-2pm</p>
    <p class="hours__row">Saturday ....... 9am-2pm</p>
    <p class="hours__row">Sunday ......... Closed</p>
  </div>

  <div class="accent-band accent-band--back-middle"></div>
  <div class="damask damask--back-bottom" role="img" aria-label="Silver damask ornament"></div>

  <p class="address">4 Marlow Parade, Surrey, KT9 3QD</p>
  <div class="map" role="img" aria-label="Street map showing the clinic location"></div>
</section>

</body>
</html>
```